Construction company needs upscale elegant truck and trailer design

Hello,
I am looking for a wrap design for my Velmark ridgeback truck and my 6x12 cargo trailer. I want to advertise my remodeling business, but I want it to be elegant and upscale. We work on commercial and residential projects with a specialization in historic homes and interior buildouts.
Our website is www.brookpierbuilders.example.
We cater to upscale clientele and I don't want it to be too flashy. I don't want anything on the back glass. I also don't want a full vehicle wrap to keep the cost down. I want a partial wrap that goes towards the back, nothing on the hood. The phone number is 555-281-3390.

Target Market(s)

Historic Restoration - New Construction - Remodeling

Industry/Entity Type

Luxury Construction Remodeling

Colors

Designer to choose colors to be used in the design.

Requirements
Must have
• truck and trailer
Nice to have
• My truck is silver with black rims, so I want it to match nice with what I already have.

```html
<!DOCTYPE html>
<html lang="en">
<head>
<meta charset="utf-8">
<title>Brookpier Builders – Truck and Trailer Graphics</title>
<link href="https://fonts.googleapis.com/css2?family=Tinos:wght@700&family=Poiret+One&family=Montserrat:ital,wght@1,800&display=swap" rel="stylesheet">
<style>
  :root{
    --page:#ececec;
    --panel:#ffffff;
    --ink:#1e1a1a;
    --yellow:#ffd21a;
    --accent:#f2b705;
  }
  html,body{margin:0;padding:0;overflow:hidden;}
  body{width:1200px;height:1200px;background:var(--page);position:relative;}
  .panel{position:absolute;background:var(--panel);box-shadow:0 2px 10px rgba(0,0,0,.12);}
  .panel svg{display:block;width:100%;height:100%;}
  .panel--truck{left:60px;top:150px;width:1080px;height:238px;}
  .panel--trailer{left:165px;top:470px;width:870px;height:502px;}
  .brand{font-family:"Tinos",serif;font-weight:700;fill:var(--ink);}
  .license{font-family:"Poiret One",sans-serif;fill:var(--ink);}
  .phone{font-family:"Montserrat",sans-serif;font-style:italic;font-weight:800;fill:var(--ink);}
  .web{font-family:"Poiret One",sans-serif;fill:var(--ink);font-weight:700;}
  .contact-box{fill:var(--yellow);}
  .stripe-art{fill:var(--ink);opacity:.85;}
  .stripe-art--accent{fill:var(--accent);opacity:1;}
</style>
</head>
<body>

<section class="panel panel--truck" aria-label="Truck side graphic">
  <svg viewBox="0 0 718 158">
    <text class="brand" x="47" y="94" font-size="34" textLength="228" lengthAdjust="spacingAndGlyphs">BROOKPIER</text>
    <text class="brand" x="47" y="125" font-size="24" textLength="228" lengthAdjust="spacingAndGlyphs">BUILDERS</text>

    <g class="contact">
      <rect class="contact-box" x="311" y="72" width="129" height="66" rx="6" role="img" aria-label="Yellow sign panel carrying the contact details"/>
      <text class="phone" x="375.5" y="104" font-size="15" text-anchor="middle" textLength="106" lengthAdjust="spacingAndGlyphs">555-281-3390</text>
      <text class="web" x="375.5" y="122" font-size="9" text-anchor="middle" textLength="100" lengthAdjust="spacingAndGlyphs">BrookpierBuilders.example</text>
    </g>

    <line x1="340" y1="43" x2="460" y2="43" stroke="var(--ink)" stroke-width="2"/>
    <line x1="345" y1="47" x2="455" y2="47" stroke="var(--ink)" stroke-width="1.5"/>
    <rect class="stripe-art" x="462" y="48" width="95" height="16" role="img" aria-label="Dark speed stripe decoration"/>
    <text class="license" x="563" y="57" font-size="7" textLength="112" lengthAdjust="spacingAndGlyphs">Certified Building Contractor #048173</text>
    <line x1="557" y1="63" x2="675" y2="63" stroke="var(--ink)" stroke-width="1.5"/>
    <line x1="500" y1="77" x2="670" y2="77" stroke="var(--accent)" stroke-width="1.5"/>
    <line x1="530" y1="90" x2="600" y2="90" stroke="var(--accent)" stroke-width="1.5"/>
    <rect class="stripe-art stripe-art--accent" x="557" y="86" width="50" height="8" role="img" aria-label="Yellow speed stripe decoration"/>
  </svg>
</section>

<section class="panel panel--trailer" aria-label="Trailer side graphic">
  <svg viewBox="0 0 544 314">
    <text class="brand" x="29" y="100" font-size="58" textLength="368" lengthAdjust="spacingAndGlyphs">BROOKPIER</text>
    <text class="brand" x="31" y="148" font-size="42" textLength="368" lengthAdjust="spacingAndGlyphs">BUILDERS</text>
    <text class="license" x="59" y="172" font-size="17" textLength="282" lengthAdjust="spacingAndGlyphs">Certified Building Contractor #048173</text>

    <g class="contact">
      <rect class="contact-box" x="349" y="178" width="180" height="92" rx="8" role="img" aria-label="Yellow sign panel carrying the contact details"/>
      <text class="phone" x="439" y="221" font-size="21" text-anchor="middle" textLength="150" lengthAdjust="spacingAndGlyphs">555-281-3390</text>
      <text class="web" x="439" y="246" font-size="13" text-anchor="middle" textLength="138" lengthAdjust="spacingAndGlyphs">BrookpierBuilders.example</text>
    </g>

    <line x1="4" y1="195" x2="121" y2="195" stroke="var(--ink)" stroke-width="2"/>
    <line x1="71" y1="200" x2="121" y2="200" stroke="var(--ink)" stroke-width="2"/>
    <rect class="stripe-art" x="124" y="199" width="95" height="18" role="img" aria-label="Dark speed stripe decoration"/>
    <line x1="221" y1="215" x2="336" y2="215" stroke="var(--ink)" stroke-width="2"/>
    <line x1="226" y1="223" x2="271" y2="223" stroke="var(--ink)" stroke-width="2"/>
    <line x1="161" y1="232" x2="331" y2="232" stroke="var(--accent)" stroke-width="1.5"/>
    <line x1="176" y1="243" x2="221" y2="243" stroke="var(--accent)" stroke-width="1.5"/>
    <rect class="stripe-art stripe-art--accent" x="221" y="235" width="47" height="8" role="img" aria-label="Yellow speed stripe decoration"/>
  </svg>
</section>

</body>
</html>
```